Chinese Herbal and Roots Shop design

Hello Designers,

We are a herbal startup company which sells Chinese Herbal Products. we are looking for a responsive and unqiue Ecommerce web design.
Our business name is velorin and our area of business cut across the entire United States.

We don't have a logo at the moment and designers who come up with a great logo is more likely to be awarded winner of the consent.

The design needs to be completely custom design and we are not after just a template design. Please be creative and at the same time design have to be professionally looking and easy to navigate.
A theme which suits a herbal products are desired. We are open to different colors excpet RED and PINK.

NAVIGATION
Header -
Home, products, offers, Blog, cart, login/account

Footer -
Please refer to other Ecommerce websites

Page requires:
HOME PAGE
1. slider(Highlist products)
2. FEATURE PRODUCTS
3. Latest products
4. Most selling products
5. Deal of the day
6. Email capture (Newsletter/signup)
7. Social media links
8. Footer

PRODUCT PAGE
All the products will be present here with required details (price, short note and offers if any)

PRODUCT DETAILS PAGE
A well designed detailed page for a particular product covers the details of the price, increment, short description, purchase and other add to cart button. A section with similar products should be listed below aswell.

Industry/Entity Type

It Company

Coding

Coded - Design and coding required

```html
<!DOCTYPE html>
<html lang="en">
<head>
<meta charset="utf-8">
<title>Velorin — Chinese Herbal Shop</title>
<link rel="stylesheet" href="https://fonts.googleapis.com/css2?family=Open+Sans:wght@400;600;700;800&display=swap">
<style>
:root{
  --orange:#f39200;
  --orange-light:#ffb03a;
  --orange-dark:#d97800;
  --green:#5fa830;
  --bg:#ececec;
  --panel:#ffffff;
  --line:#dddddd;
  --text:#555555;
  --muted:#888888;
  --dark:#333333;
  --nav-top:#6c6c6c;
  --nav-bottom:#4a4a4a;
}
*{box-sizing:border-box;margin:0;padding:0}
html,body{width:1200px;height:2556px;overflow:hidden}
body{background:var(--bg);font-family:"Open Sans",Arial,sans-serif;color:var(--text);font-size:14px}
.page{width:1024px;margin:0 auto;position:relative;height:2556px}

/* header */
.header{height:160px;position:relative}
.brand{position:absolute;left:0;top:68px;display:flex;align-items:center;gap:12px}
.brand-mark{width:28px;height:28px;border-radius:50%;background:var(--green)}
.brand-name{font-size:58px;font-weight:800;color:var(--orange);letter-spacing:-1px;line-height:1}
.social-top{position:absolute;right:0;top:60px;display:flex;gap:10px}
.social-dot{width:26px;height:26px;border-radius:50%;background:#c9c9c9}
.account-links{position:absolute;right:0;top:104px;display:flex;gap:18px;font-size:15px;font-weight:600;color:var(--dark)}
.account-links a{color:inherit;text-decoration:none}
.account-links a.active{color:var(--orange)}

/* nav */
.nav{height:56px;background:linear-gradient(var(--nav-top),var(--nav-bottom));display:flex;align-items:center;justify-content:space-between;border-radius:3px}
.menu{display:flex;height:100%}
.menu a{display:flex;align-items:center;padding:0 28px;color:#fff;font-weight:700;font-size:15px;text-decoration:none}
.menu a.active{background:var(--orange)}
.nav-tools{display:flex;gap:12px;padding-right:12px}
.cart{background:var(--orange);color:#fff;font-size:14px;font-weight:700;padding:8px 16px;border-radius:3px;width:210px}
.cart span{font-weight:400}
.search{display:flex;width:250px;border-radius:3px;overflow:hidden}
.search-label{background:var(--orange);color:#fff;font-weight:700;padding:8px 12px;font-size:13px}
.search-field{flex:1;background:#fff}

/* slider */
.slider{margin-top:12px;height:368px;display:flex;background:var(--panel);position:relative}
.slide-main{flex:0 0 600px;position:relative;background:linear-gradient(90deg,#fff 55%,#f3f8ea)}
.slide-product{position:absolute;left:70px;top:30px;width:230px;height:290px;border-radius:14px;background:linear-gradient(#f2f2f2,#d8d8d8 60%,#3a55a8 60%,#2a3f82)}
.slide-leaves{position:absolute;right:0;top:0;width:160px;height:200px;background:linear-gradient(160deg,#b9db7a,#f0f8e2 70%,transparent)}
.slide-copy{position:absolute;left:340px;top:90px}
.slide-brand{color:var(--green);font-weight:700;font-size:16px;letter-spacing:1px}
.slide-title{font-size:34px;font-weight:800;color:var(--dark);line-height:1.05;margin-top:4px}
.slide-sub{font-size:13px;color:var(--muted);margin-top:6px}
.slide-buy{display:flex;margin-top:20px;gap:8px}
.price-big{background:var(--orange);color:#fff;font-size:30px;font-weight:800;padding:6px 18px;border-radius:3px}
.buy-btn{width:52px;background:var(--green);border-radius:3px;display:flex;align-items:center;justify-content:center}
.slide-side{flex:1;background:var(--orange);position:relative;overflow:hidden}
.slide-flowers{position:absolute;left:0;right:0;bottom:0;height:200px;background:radial-gradient(circle at 30% 70%,#ffd23a,#f7a400 40%,transparent 70%),radial-gradient(circle at 80% 60%,#ffe066,#f39200 45%,transparent 70%)}
.slide-side-copy{position:absolute;left:40px;top:40px;color:#fff;font-weight:800;font-size:40px;line-height:1.05}
.slide-side-copy small{display:block;font-size:26px;font-weight:700}
.dots{position:absolute;left:540px;bottom:16px;display:flex;gap:8px}
.dots i{width:14px;height:14px;border-radius:50%;background:#ccc}
.dots i.on{background:var(--orange)}

/* promo banners */
.promos{margin-top:20px;height:170px;display:grid;grid-template-columns:repeat(3,1fr);gap:12px}
.promo{position:relative;background:#fff;overflow:hidden;padding:24px 24px 0}
.promo-art{position:absolute;top:0;bottom:0;width:140px}
.promo-1 .promo-art{left:0;background:radial-gradient(circle at 30% 50%,#ffd43a,#f7a400 55%,#fff 72%)}
.promo-2 .promo-art{left:0;background:radial-gradient(circle at 35% 50%,#fff,#e7ecd9 55%,#fff 72%)}
.promo-3 .promo-art{right:0;background:radial-gradient(circle at 70% 50%,#ffe066,#f39200 55%,#fff 72%)}
.promo-copy{position:relative;text-align:right}
.promo-3 .promo-copy{text-align:left}
.promo-copy .p1{font-size:30px;font-weight:800;color:var(--dark);line-height:1}
.promo-copy .p2{font-size:26px;font-weight:800;color:var(--orange);line-height:1.1}
.promo-copy .p3{font-size:13px;color:var(--muted)}
.promo-btn{display:inline-block;margin-top:10px;background:var(--orange);color:#fff;font-size:12px;font-weight:700;padding:6px 14px;border-radius:3px}

/* product sections */
.section{background:var(--panel);margin-top:20px;padding:20px 24px 24px}
.section-title{font-size:16px;font-weight:800;color:var(--dark);text-transform:uppercase;border-bottom:1px solid var(--line);padding-bottom:12px;margin-bottom:20px}
.section-title em{font-style:normal;color:var(--orange)}
.products{display:grid;grid-template-columns:repeat(4,1fr);gap:20px}
.card{border:1px solid var(--line);padding:14px}
.card-title{font-size:13px;font-weight:700;color:var(--dark);height:40px;line-height:1.4}
.card-title.hot{color:var(--orange)}
.card-image{height:190px;margin:10px 0}
.img-a{background:linear-gradient(#fff,#eef3f8 30%,#2f6db5 70%,#fff)}
.img-b{background:linear-gradient(#fff,#e8e8e8 20%,#d94b2b 55%,#f0f0f0 80%,#fff)}
.img-c{background:linear-gradient(#fff,#f3e9c6 30%,#a33 60%,#fff)}
.img-d{background:linear-gradient(#fff,#2a2a2a 25%,#1a1a1a 70%,#4c9a2a 78%,#fff)}
.img-e{background:linear-gradient(#fff,#f6f6f6 20%,#e8b81c 55%,#fff)}
.img-f{background:linear-gradient(#fff,#fdfbe8 20%,#d89a1c 55%,#fff)}
.img-g{background:linear-gradient(#fff,#eef0f4 20%,#c62828 45%,#f5f5f5 75%,#fff)}
.img-h{background:linear-gradient(#fff,#fdf3d4 20%,#2e7d32 50%,#f4c430 70%,#fff)}
.price{display:inline-block;background:var(--orange);color:#fff;font-weight:800;font-size:18px;padding:4px 14px;border-radius:2px;width:100%}
.card-desc{font-size:11px;color:var(--muted);line-height:1.5;margin:10px 0;height:50px}
.details{display:inline-block;font-size:11px;font-weight:700;color:var(--dark);border:1px solid var(--line);background:#f3f3f3;padding:5px 12px}
.details.dark{background:#555;color:#fff;border-color:#555}

/* footer */
.footer{margin-top:20px;background:var(--panel);padding:18px 24px;display:grid;grid-template-columns:repeat(4,1fr);gap:24px;height:150px}
.footer h4{font-size:13px;font-weight:800;color:var(--orange);text-transform:uppercase;margin-bottom:8px}
.footer p,.footer li{font-size:11px;color:var(--muted);line-height:1.6;list-style:none}
.newsletter-field{display:flex;margin-top:6px;border:1px solid var(--line)}
.newsletter-field span{flex:1;font-size:11px;color:var(--muted);padding:6px}
.newsletter-field b{background:#eee;font-size:11px;padding:6px 10px;color:var(--dark)}
.bottom{display:flex;justify-content:space-between;align-items:center;height:46px;font-size:12px;color:var(--muted)}
.bottom strong{color:var(--orange)}
.social-bottom{display:flex;gap:10px}
.social-bottom i{width:24px;height:24px;border-radius:50%;background:var(--orange)}
</style>
</head>
<body>
<div class="page">

  <header class="header">
    <div class="brand"><span class="brand-mark"></span><span class="brand-name">Velorin</span></div>
    <div class="social-top"><span class="social-dot"></span><span class="social-dot"></span><span class="social-dot"></span></div>
    <nav class="account-links">
      <a class="active" href="#">Register</a><a href="#">Login</a><a href="#">Delivery</a><a href="#">Checkout</a><a href="#">My Account</a>
    </nav>
  </header>

  <div class="nav">
    <div class="menu">
      <a class="active" href="#">HOME</a><a href="#">PRODUCTS</a><a href="#">OFFERS</a><a href="#">BLOG</a>
    </div>
    <div class="nav-tools">
      <div class="cart">CART: <span>no items</span></div>
      <div class="search"><span class="search-label">SEARCH</span><span class="search-field"></span></div>
    </div>
  </div>

  <section class="slider">
    <div class="slide-main">
      <div class="slide-leaves" role="img" aria-label="Green bamboo leaves"></div>
      <div class="slide-product" role="img" aria-label="Herbal supplement bottle"></div>
      <div class="slide-copy">
        <div class="slide-brand">VERDANT LABS</div>
        <div class="slide-title">Ginseng<br>Ultra</div>
        <div class="slide-sub">90 capsules</div>
        <div class="slide-buy">
          <span class="price-big">$ 28.99</span>
          <span class="buy-btn"><svg width="28" height="24" viewBox="0 0 28 24"><path d="M1 2h5l3 13h14l3-9H8" fill="none" stroke="#fff" stroke-width="2.5"/><circle cx="11" cy="20" r="2" fill="#fff"/><circle cx="21" cy="20" r="2" fill="#fff"/></svg></span>
        </div>
      </div>
    </div>
    <div class="slide-side">
      <div class="slide-flowers" role="img" aria-label="Yellow and orange daisies"></div>
      <div class="slide-side-copy">Learn how<br>WE CAN HELP<small>you today!</small></div>
    </div>
    <div class="dots"><i class="on"></i><i></i><i></i></div>
  </section>

  <section class="promos">
    <div class="promo promo-1"><div class="promo-art" role="img" aria-label="Orange slices"></div>
      <div class="promo-copy"><div class="p1">Special offer</div><div class="p2">20% off</div><span class="promo-btn">Shop now</span></div></div>
    <div class="promo promo-2"><div class="promo-art" role="img" aria-label="White flower"></div>
      <div class="promo-copy"><div class="p1">SALE</div><div class="p2">Up to 50% off</div><span class="promo-btn">Shop now</span></div></div>
    <div class="promo promo-3"><div class="promo-art" role="img" aria-label="Yellow gerbera"></div>
      <div class="promo-copy"><div class="p1">FREE<br>SHIPPING</div><div class="p3">on orders over $99</div><span class="promo-btn">Shop now</span></div></div>
  </section>

  <section class="section">
    <h2 class="section-title"><em>Featured</em> products</h2>
    <div class="products">
      <div class="card"><div class="card-title hot">Red ginseng root daily tonic</div><div class="card-image img-a" role="img" aria-label="Ginseng product box"></div><span class="price">$25.00</span><p class="card-desc">Gentle herbal blend for daily balance, crafted from roots and leaves.</p><span class="details dark">Details</span></div>
      <div class="card"><div class="card-title">Astragalus root immune support</div><div class="card-image img-b" role="img" aria-label="Herbal tablet bottle"></div><span class="price">$25.00</span><p class="card-desc">Gentle herbal blend for daily balance, crafted from roots and leaves.</p><span class="details">Details</span></div>
      <div class="card"><div class="card-title">Licorice root calming herbal tea</div><div class="card-image img-c" role="img" aria-label="Herbal tea box"></div><span class="price">$25.00</span><p class="card-desc">Gentle herbal blend for daily balance, crafted from roots and leaves.</p><span class="details">Details</span></div>
      <div class="card"><div class="card-title">Reishi mushroom extract capsules jar</div><div class="card-image img-d" role="img" aria-label="Dark supplement jar"></div><span class="price">$25.00</span><p class="card-desc">Gentle herbal blend for daily balance, crafted from roots and leaves.</p><span class="details">Details</span></div>
    </div>
  </section>

  <section class="section">
    <h2 class="section-title"><em>Latest</em> products</h2>
    <div class="products">
      <div class="card"><div class="card-title">Goji berry energy herbal blend</div><div class="card-image img-e" role="img" aria-label="Herbal capsule bottle"></div><span class="price">$25.00</span><p class="card-desc">Gentle herbal blend for daily balance, crafted from roots and leaves.</p><span class="details">Details</span></div>
      <div class="card"><div class="card-title">Dong quai root women's tonic</div><div class="card-image img-f" role="img" aria-label="Herbal oil bottle"></div><span class="price">$25.00</span><p class="card-desc">Gentle herbal blend for daily balance, crafted from roots and leaves.</p><span class="details">Details</span></div>
      <div class="card"><div class="card-title">Ginger root warming digestive tablets</div><div class="card-image img-g" role="img" aria-label="Herbal tablet box"></div><span class="price">$25.00</span><p class="card-desc">Gentle herbal blend for daily balance, crafted from roots and leaves.</p><span class="details">Details</span></div>
      <div class="card"><div class="card-title">Green tea leaf antioxidant pack</div><div class="card-image img-h" role="img" aria-label="Herbal tablet packet"></div><span class="price">$25.00</span><p class="card-desc">Gentle herbal blend for daily balance, crafted from roots and leaves.</p><span class="details">Details</span></div>
    </div>
  </section>

  <section class="section">
    <h2 class="section-title"><em>Best selling</em> products</h2>
    <div class="products">
      <div class="card"><div class="card-title hot">Red ginseng root daily tonic</div><div class="card-image img-a" role="img" aria-label="Ginseng product box"></div><span class="price">$25.00</span><p class="card-desc">Gentle herbal blend for daily balance, crafted from roots and leaves.</p><span class="details dark">Details</span></div>
      <div class="card"><div class="card-title">Astragalus root immune support</div><div class="card-image img-b" role="img" aria-label="Herbal tablet bottle"></div><span class="price">$25.00</span><p class="card-desc">Gentle herbal blend for daily balance, crafted from roots and leaves.</p><span class="details">Details</span></div>
      <div class="card"><div class="card-title">Licorice root calming herbal tea</div><div class="card-image img-c" role="img" aria-label="Herbal tea box"></div><span class="price">$25.00</span><p class="card-desc">Gentle herbal blend for daily balance, crafted from roots and leaves.</p><span class="details">Details</span></div>
      <div class="card"><div class="card-title">Reishi mushroom extract capsules jar</div><div class="card-image img-d" role="img" aria-label="Dark supplement jar"></div><span class="price">$25.00</span><p class="card-desc">Gentle herbal blend for daily balance, crafted from roots and leaves.</p><span class="details">Details</span></div>
    </div>
  </section>

  <footer class="footer">
    <div><h4>About</h4><p>Velorin brings classic Chinese herbs and roots to homes across the United States with care.</p></div>
    <div><h4>Categories</h4><ul><li>Roots and barks</li><li>Herbal teas blends</li><li>Mushroom extracts daily</li><li>Capsules and tablets</li><li>Oils and balms</li><li>Gift sets range</li></ul></div>
    <div><h4>Information</h4><ul><li>About us</li><li>Delivery info</li><li>Privacy policy</li><li>Terms apply</li><li>Contact us</li><li>Site map</li></ul></div>
    <div><h4>Newsletter</h4><p>Sign up for deals</p><div class="newsletter-field"><span>Enter your email</span><b>Go</b></div></div>
  </footer>
  <div class="bottom">
    <span>Copyright 2017 <strong>Velorin</strong>. All right reserved</span>
    <div class="social-bottom"><i></i><i></i><i></i></div>
  </div>

</div>
</body>
</html>
```